Exhibition/ Conference Booth Design.

To design a background for our booth at an upcoming conference incorporating our logo. We're a market leader in the automation industry for lead-acid batteries. This includes UPS, automobiles, reserve power and traction. The design could be as simple as incorporating our logo into a design to fit our booth that shows we're forward-thinking, innovative future thinking or going into more detail about the different usages for lead-acid batteries.

*Market Leader
*R&D

Company Profile -

KWR is a market-leading supplier of Assembly and Plate Manufacturing equipment that is dedicated to helping businesses of all sizes thrive in today's ever-changing world. With our comprehensive range of products and services, our customer-centric approach, and our commitment to innovation, we are a proven, trusted partner for companies across the globe.

At KWR we are committed to our customers' success. That's why we work closely with them to understand their unique requirements, goals, and challenges, and tailor our solutions to meet their specific needs.

Innovation is at the heart of everything we do at KWR. We invest heavily in research and development to stay ahead of the curve, and we regularly introduce new features, upgrades, and solutions that anticipate our customers' evolving needs. Our commitment to innovation has earned us a reputation as a leader in the industry, and we are constantly exploring new technologies and trends to help our customers succeed.

Industry/Entity Type

Automation - Lead Acid - Engineering

Requirements
Must have
• Our Logo
Nice to have
• Hi All, some good potentials here but I’m wondering if I could update the brief to be more ‘green’ eco friendly - Incorporting where we use Lead Acid batteries. i.e Energy storage, reserve power, automobiles, traction wind/solar and the fact lead acid is widely recyclable. It would be good to see if any of you have some ideas of how to incorporate the logo into this also. Possibly doing something different with the logo colours also.

```html
<!DOCTYPE html>
<html lang="en">
<head>
<meta charset="utf-8">
<title>KWR Booth Backdrop</title>
<link href="https://fonts.googleapis.com/css2?family=Montserrat:ital,wght@0,800;1,700&display=swap" rel="stylesheet">
<style>
  :root {
    --page: #ffffff;
    --green-bright: #22c55e;
    --green-edge: #2cc45b;
    --green-mid: #23c04f;
    --green-deep: #038641;
    --brand-blue: #1f5c9e;
    --brand-red: #e4002b;
    --ink: #000000;
  }
  html, body {
    margin: 0;
    padding: 0;
    width: 1200px;
    height: 999px;
    overflow: hidden;
    background: var(--page);
  }
  .canvas {
    position: relative;
    width: 1200px;
    height: 999px;
  }
  .banner {
    position: absolute;
    left: 38px;
    top: 258px;
    width: 1125px;
    height: 474px;
    overflow: hidden;
    background: radial-gradient(ellipse 640px 520px at 440px 160px,
      #ffffff 0%, #ffffff 38%, #d9f3de 62%, #8fe0a2 82%, var(--green-edge) 100%);
  }
  .banner-art {
    position: absolute;
    inset: 0;
  }
  .wordmark {
    position: absolute;
    left: 150px;
    top: 62px;
    margin: 0;
    font-family: "Montserrat", sans-serif;
    font-weight: 800;
    font-size: 136px;
    line-height: 1;
    letter-spacing: 4px;
    color: var(--brand-red);
  }
  .tagline {
    position: absolute;
    left: 116px;
    top: 256px;
    margin: 0;
    font-family: "Montserrat", sans-serif;
    font-style: italic;
    font-weight: 700;
    font-size: 37px;
    line-height: 1;
    letter-spacing: 1.5px;
    white-space: nowrap;
  }
  .tagline .automation { color: var(--brand-blue); }
  .tagline .lead-acid { color: var(--ink); }
  .tagline .engineering { color: var(--brand-red); }
</style>
</head>
<body>
<div class="canvas">
  <section class="banner">
    <svg class="banner-art" width="1125" height="474" viewBox="0 0 1125 474" xmlns="http://www.w3.org/2000/svg">
      <defs>
        <linearGradient id="turbineTone" x1="0" y1="0" x2="1" y2="0">
          <stop offset="0" stop-color="#22c55e" stop-opacity="0"/>
          <stop offset="0.5" stop-color="#22c55e" stop-opacity="0.35"/>
          <stop offset="1" stop-color="#0b8f45" stop-opacity="0.5"/>
        </linearGradient>
      </defs>
      <rect class="turbine-area" x="752" y="0" width="373" height="350" fill="url(#turbineTone)"
            role="img" aria-label="Two green wind turbines standing on the hilltop"/>
      <polygon class="hill-light" points="0,474 562,354 680,347 1125,320 1125,474" fill="var(--green-mid)"/>
      <polygon class="hill-deep" points="0,474 860,336 1125,354 1125,474" fill="var(--green-deep)"/>
    </svg>
    <h1 class="wordmark">KWR</h1>
    <p class="tagline">
      <span class="automation">AUTOMATION</span>
      <span class="lead-acid">. LEAD ACID</span>
      <span class="engineering">. ENGINEERING</span>
    </p>
  </section>
</div>
</body>
</html>
```